LED Bulb Packaging

We require a retail box design so some led lighting. The concept must be uniform accross a nuimber of sizes with technical information and Actual bulb image replaceable.

```html
<!DOCTYPE html>
<html lang="en">
<head>
<meta charset="utf-8">
<title>LED Corn Light Retail Box – 54W Dieline</title>
<link href="https://fonts.googleapis.com/css2?family=Arimo:wght@400;700&family=Noto+Serif+SC:wght@400&display=swap" rel="stylesheet">
<style>
  :root{
    --paper:#ffffff;
    --dieline:#c0392b;
    --flap:#21608f;
    --panel-dark:#0a2346;
    --panel-light:#6fc0ee;
    --accent:#f08a1c;
    --text-light:#ffffff;
    --title-red:#e0262b;
    --cert:#e8edf3;
  }
  *{margin:0;padding:0;box-sizing:border-box}
  html,body{width:1200px;height:705px;overflow:hidden;background:var(--paper)}
  body{font-family:"Arimo",Arial,sans-serif;position:relative}
  .sheet{position:absolute;inset:0;border:1px solid #999}
  .size-title{position:absolute;left:258px;top:62px;font-size:62px;color:var(--title-red);
    font-family:"Arimo","Noto Serif SC",serif;letter-spacing:1px;white-space:nowrap}
  .dieline{position:absolute;left:0;top:0}
  .abs{position:absolute}
  .brand-led{font-weight:700;color:var(--accent);letter-spacing:2px;line-height:1}
  .brand-sub{color:var(--text-light);font-weight:700;line-height:1}
  .spec-value{color:var(--accent);font-weight:700;font-size:12px;line-height:1}
  .spec-label{color:var(--text-light);font-size:5px;line-height:1.2}
  .upto{color:var(--text-light);font-size:4px;line-height:1;display:inline-block;width:9px;vertical-align:middle}
  .cert-row{display:flex;gap:6px;align-items:center}
  .cert{width:12px;height:12px;border-radius:50%;background:var(--cert)}
  .cert.square{border-radius:2px;width:14px}
  .product-shot{border-radius:14px 40px 40px 14px;
    background:linear-gradient(180deg,#3b4450 0%,#c9d3dc 22%,#f2f6f9 50%,#b7c3ce 78%,#2f3741 100%)}
  .note-title{color:var(--accent);font-weight:700;font-size:11px}
  .note-list{color:var(--text-light);font-size:4.6px;line-height:1.35;list-style:none}
  .energy-card{background:#fff;padding:3px;width:42px;height:45px}
  .energy-bar{height:4px;margin-bottom:1px;font-size:3.5px;color:#fff;padding-left:1px;line-height:4px}
  .side-power{color:var(--accent);font-weight:700;font-size:34px}
  .side-specs{color:var(--text-light);font-size:8px;word-spacing:6px}
  .lid{left:612px;top:205px;width:398px;height:155px;transform:rotate(180deg)}
  .feature{position:absolute;top:70px;width:44px;margin-left:-22px;text-align:center}
  .feature-dot{width:18px;height:18px;border-radius:50%;background:var(--accent);margin:0 auto 5px;
    display:flex;align-items:center;justify-content:center}
  .feature-dot span{width:8px;height:8px;border:1.5px solid #fff;border-radius:50%}
  .feature-label{color:var(--text-light);font-size:4.6px;line-height:1.2}
</style>
</head>
<body>
<div class="sheet">
  <div class="size-title">54W尺寸：305*120*120mm</div>

  <svg class="dieline" width="1200" height="705" viewBox="0 0 1200 705" aria-hidden="true">
    <defs>
      <radialGradient id="panelBurst" cx="0.7" cy="0.45" r="0.75">
        <stop offset="0" stop-color="var(--panel-light)"/>
        <stop offset="0.45" stop-color="#1f5f9b"/>
        <stop offset="1" stop-color="var(--panel-dark)"/>
      </radialGradient>
      <radialGradient id="lidBurst" cx="0.45" cy="0.5" r="0.7">
        <stop offset="0" stop-color="#4aa5dd"/>
        <stop offset="0.5" stop-color="#1a4f85"/>
        <stop offset="1" stop-color="var(--panel-dark)"/>
      </radialGradient>
    </defs>
    <g fill="var(--flap)" stroke="var(--dieline)" stroke-width="0.8">
      <!-- glue flap -->
      <polygon points="65,372 33,380 33,498 65,505"/>
      <!-- top flaps -->
      <polygon points="65,360 150,270 458,270 458,360" fill="url(#lidBurst)"/>
      <polygon points="460,360 545,270 612,270 612,360"/>
      <polygon points="1010,360 1010,270 1080,270 1163,360"/>
      <!-- handle tab -->
      <path d="M733,205 L733,186 Q733,180 740,180 L882,180 Q888,180 888,186 L888,205 Z" fill="#fff"/>
      <!-- bottom flaps -->
      <polygon points="65,516 147,598 147,625 380,625 380,598 460,516"/>
      <polygon points="460,516 612,516 612,598 540,598 460,530"/>
      <polygon points="612,516 612,625 695,625 695,598 930,598 930,625 1010,625 1010,516"/>
      <polygon points="1010,516 1163,516 1163,530 1085,598 1010,598"/>
      <!-- main panels -->
      <rect x="65" y="360" width="395" height="156" fill="url(#panelBurst)"/>
      <rect x="460" y="360" width="152" height="156" fill="url(#lidBurst)"/>
      <rect x="612" y="205" width="398" height="155" fill="url(#lidBurst)"/>
      <rect x="612" y="360" width="398" height="156" fill="url(#panelBurst)"/>
      <rect x="1010" y="360" width="153" height="156" fill="url(#lidBurst)"/>
    </g>
    <!-- handle cutouts -->
    <path d="M230,360 L230,333 Q230,327 236,327 L286,327 Q292,327 292,333 L292,360" fill="#fff" stroke="var(--dieline)" stroke-width="0.8"/>
    <rect x="735" y="188" width="150" height="14" rx="3" fill="#fff" stroke="var(--dieline)" stroke-width="0.6"/>
    <!-- accent rules -->
    <line x1="140" y1="287" x2="458" y2="287" stroke="var(--accent)" stroke-width="3"/>
    <line x1="460" y1="287" x2="612" y2="287" stroke="var(--accent)" stroke-width="3"/>
    <line x1="1010" y1="287" x2="1090" y2="287" stroke="var(--accent)" stroke-width="3"/>
  </svg>

  <!-- top flap branding -->
  <div class="abs brand-led" style="left:235px;top:295px;font-size:17px">LED</div>
  <div class="abs brand-sub" style="left:236px;top:314px;font-size:6px;color:#fff">CORN LIGHT</div>

  <!-- front panel -->
  <div class="abs brand-led" style="left:79px;top:376px;font-size:34px">LED</div>
  <div class="abs brand-sub" style="left:80px;top:411px;font-size:12px">CORN LIGHT</div>
  <div class="abs" style="left:80px;top:443px">
    <div class="spec-value">120lm/w</div><div class="spec-label">Luminous efficiency</div>
  </div>
  <div class="abs" style="left:166px;top:443px">
    <div class="spec-value"><span class="upto">UP TO</span>85%</div><div class="spec-label">Energy Saving</div>
  </div>
  <div class="abs" style="left:80px;top:463px">
    <div class="spec-value">50000hrs</div><div class="spec-label">Lifespan</div>
  </div>
  <div class="abs" style="left:166px;top:463px"><div class="spec-value">IP64</div></div>
  <div class="abs cert-row" style="left:80px;top:490px">
    <div class="cert"></div><div class="cert"></div><div class="cert square"></div><div class="cert"></div><div class="cert"></div><div class="cert square"></div>
  </div>
  <div class="abs product-shot" role="img" aria-label="Product photo: LED corn light bulb" style="left:258px;top:396px;width:185px;height:104px"></div>

  <!-- side panel: notes -->
  <div class="abs" style="left:463px;top:368px;width:145px">
    <div class="note-title">Note:</div>
    <ol class="note-list">
      <li>1.Before install or replace the lamps please cut off the switch.</li>
      <li>2.After installed,when lamp work normal,pls note not take off the driver with electricity on.</li>
      <li>3.After lighting a long time,the lamps can be reach 60°C,Pls be careful to take off the lamps avoid scald.</li>
      <li>4.Interior driver is constant current.</li>
      <li>5.Work temperature is -20~40°C.</li>
    </ol>
  </div>
  <div class="abs energy-card" style="left:465px;top:445px">
    <div style="font-size:5px;color:#1a7b3c;font-weight:700;margin-bottom:1px">Energy <span style="background:#222;color:#fff;padding:0 2px">A</span></div>
    <div class="energy-bar" style="width:10px;background:#0a9a3f">A</div>
    <div class="energy-bar" style="width:13px;background:#4eb748">B</div>
    <div class="energy-bar" style="width:16px;background:#b6d333">C</div>
    <div class="energy-bar" style="width:19px;background:#f6e71c">D</div>
    <div class="energy-bar" style="width:22px;background:#f5a623">E</div>
    <div class="energy-bar" style="width:25px;background:#e8601c">F</div>
    <div class="energy-bar" style="width:28px;background:#d7191c">G</div>
  </div>

  <!-- lid (printed upside down) -->
  <div class="abs lid">
    <div class="abs brand-led" style="left:172px;top:20px;font-size:21px">LED</div>
    <div class="abs brand-sub" style="left:172px;top:43px;font-size:7px">CORN LIGHT</div>
    <div class="feature" style="left:70px"><div class="feature-dot"><span></span></div><div class="feature-label">High Brightness</div></div>
    <div class="feature" style="left:107px"><div class="feature-dot"><span></span></div><div class="feature-label">Longlife</div></div>
    <div class="feature" style="left:145px"><div class="feature-dot"><span></span></div><div class="feature-label">Security</div></div>
    <div class="feature" style="left:183px"><div class="feature-dot"><span></span></div><div class="feature-label">Energy Saving</div></div>
    <div class="feature" style="left:221px"><div class="feature-dot"><span></span></div><div class="feature-label">Protect Your Eyes</div></div>
    <div class="feature" style="left:258px"><div class="feature-dot"><span></span></div><div class="feature-label">Low-carbon Green</div></div>
    <div class="feature" style="left:296px"><div class="feature-dot"><span></span></div><div class="feature-label">No Flicker Free</div></div>
    <div class="feature" style="left:333px"><div class="feature-dot"><span></span></div><div class="feature-label">No Radiation</div></div>
  </div>

  <!-- back panel -->
  <div class="abs brand-led" style="left:627px;top:376px;font-size:34px">LED</div>
  <div class="abs brand-sub" style="left:628px;top:411px;font-size:12px">CORN LIGHT</div>
  <div class="abs" style="left:628px;top:443px">
    <div class="spec-value">120lm/w</div><div class="spec-label">Luminous efficiency</div>
  </div>
  <div class="abs" style="left:714px;top:443px">
    <div class="spec-value"><span class="upto">UP TO</span>85%</div><div class="spec-label">Energy Saving</div>
  </div>
  <div class="abs" style="left:628px;top:463px">
    <div class="spec-value">50000hrs</div><div class="spec-label">Lifespan</div>
  </div>
  <div class="abs" style="left:714px;top:463px"><div class="spec-value">IP64</div></div>
  <div class="abs cert-row" style="left:628px;top:490px">
    <div class="cert"></div><div class="cert"></div><div class="cert square"></div><div class="cert"></div><div class="cert"></div><div class="cert square"></div>
  </div>
  <div class="abs product-shot" role="img" aria-label="Product photo: LED corn light bulb" style="left:805px;top:396px;width:185px;height:104px"></div>

  <!-- side panel: wattage -->
  <div class="abs side-power" style="left:1043px;top:428px">54W</div>
  <div class="abs side-specs" style="left:1020px;top:481px">•50000hrs •IP64 •120lm/w</div>
</div>
</body>
</html>
```